Business Card and Logo tweak for a Language Boarding School

we are a boadring langauge school for under 18 international student.
We call ourselves " HCSC" - Harwick Crossway Study Centre
We are one of the TQ "tidewater quarters" Melbourne campus for TQ high school preparation program.

our address is 14 Orrin Lane Brighton 3187
Ph: 03 95550142
Email: info@myhcsc-example.com
Website: www.myhcsc-example.com

We have our HCSC logo, but not very satisfied. May be you can tweak it furhter with the fond or formations.

Basically the business card list all relevant info on one side and list all our programs on the other side.

The program we have:
ELICOS with Boarding for U18 Students
HSP-High School Preparation Program
PSP- Primary School Preparation Program
Junior Holiday Program & Study Tours
After School Tutoring
Student Wellbeing and Counselling

```html
<!DOCTYPE html>
<html lang="en">
<head>
<meta charset="utf-8">
<title>Harwick Crossway Study Centre – Business Card</title>
<link href="https://fonts.googleapis.com/css2?family=Arimo:wght@400;700&display=swap" rel="stylesheet">
<style>
  :root {
    --stage: #c9c9c9;
    --card-white: #ffffff;
    --card-dark: #262626;
    --ink: #1e1e1e;
    --light-text: #f2f2f2;
    --soft-text: #cfcfcf;
    --edge: #f5a623;
    --phone: #2bc4d8;
    --mail: #e3263f;
    --web: #f0a01e;
    --pin: #a6d82a;
    --bullet: #e0e0e0;
  }
  * { box-sizing: border-box; margin: 0; padding: 0; }
  html, body { width: 1200px; height: 800px; overflow: hidden; }
  body {
    background: linear-gradient(135deg, #b3b3b3 0%, var(--stage) 50%, #dcdcdc 100%);
    font-family: "Arimo", Arial, sans-serif;
    display: flex;
    align-items: center;
    justify-content: center;
    gap: 40px;
  }
  .card {
    position: relative;
    width: 540px;
    height: 320px;
    border-radius: 18px;
    overflow: hidden;
    border-bottom: 3px solid var(--edge);
    box-shadow: 0 10px 24px rgba(0,0,0,.25);
  }

  /* Shared stacked name */
  .stacked-name {
    position: absolute;
    font-weight: 400;
    font-size: 20px;
    line-height: 22px;
    letter-spacing: .5px;
    text-transform: uppercase;
  }
  .stacked-name b { font-weight: 700; font-size: 23px; }

  /* Front */
  .card--front { background: var(--card-white); color: var(--ink); }
  .card--front .stacked-name { left: 34px; top: 26px; }
  .contact-band {
    position: absolute;
    left: 0; bottom: 30px;
    width: 310px; height: 130px;
    background: var(--card-dark);
    padding: 14px 0 0 30px;
    list-style: none;
  }
  .contact-band li {
    display: flex; align-items: center; gap: 10px;
    color: var(--light-text);
    font-size: 15px;
    height: 27px;
    white-space: nowrap;
  }
  .contact-icon { width: 22px; height: 22px; flex: none; }
  .top-band {
    position: absolute;
    right: 0; top: 36px;
    width: 150px; height: 58px;
    background: var(--card-dark);
  }
  .brand-mark {
    position: absolute;
    right: 30px; top: 172px;
    display: flex; align-items: center; gap: 12px;
    font-size: 46px; font-weight: 700;
    line-height: 1;
    color: var(--ink);
    letter-spacing: 1px;
  }
  .brand-mark .dot {
    width: 26px; height: 26px; border-radius: 50%;
    border: 4px solid var(--ink);
    flex: none;
  }

  /* Back */
  .card--back { background: var(--card-dark); color: var(--light-text); }
  .card--back .stacked-name { left: 120px; top: 34px; color: var(--soft-text); }
  .card--back .stacked-name b { color: var(--light-text); }
  .program-list {
    position: absolute;
    left: 120px; top: 136px;
    list-style: none;
  }
  .program-list li {
    display: flex; align-items: center; gap: 12px;
    font-size: 16px;
    height: 27px;
    white-space: nowrap;
  }
  .program-list li::before {
    content: "";
    width: 9px; height: 9px; border-radius: 50%;
    border: 2px solid var(--bullet);
    flex: none;
  }
</style>
</head>
<body>

<section class="card card--front" aria-label="Business card front">
  <h1 class="stacked-name">
    <b>H</b>arwick<br><b>C</b>rossway<br><b>S</b>tudy<br><b>C</b>entre
  </h1>

  <div class="top-band"></div>
  <div class="brand-mark"><span class="dot"></span>HCSC</div>

  <ul class="contact-band">
    <li>
      <svg class="contact-icon" viewBox="0 0 22 22"><circle cx="11" cy="11" r="10" fill="none" stroke="#fff" stroke-width="1.5"/><path d="M7 6l2.5 0 1 3-1.5 1a6 6 0 0 0 3 3l1-1.5 3 1V15a1.5 1.5 0 0 1-1.5 1.5A9 9 0 0 1 5.5 7.5 1.5 1.5 0 0 1 7 6z" fill="var(--phone)"/></svg>
      03 95550142
    </li>
    <li>
      <svg class="contact-icon" viewBox="0 0 22 22"><circle cx="11" cy="11" r="10" fill="none" stroke="#fff" stroke-width="1.5"/><rect x="5" y="7" width="12" height="8" fill="var(--mail)"/><path d="M5 7l6 5 6-5" fill="none" stroke="#fff" stroke-width="1"/></svg>
      info@myhcsc-example.com
    </li>
    <li>
      <svg class="contact-icon" viewBox="0 0 22 22"><circle cx="11" cy="11" r="10" fill="none" stroke="#fff" stroke-width="1.5"/><circle cx="11" cy="11" r="6" fill="var(--web)"/><path d="M5 11h12M11 5v12M7 8h8M7 14h8" stroke="#262626" stroke-width=".8" fill="none"/></svg>
      www.myhcsc-example.com
    </li>
    <li>
      <svg class="contact-icon" viewBox="0 0 22 22"><circle cx="11" cy="11" r="10" fill="none" stroke="#fff" stroke-width="1.5"/><path d="M11 17s-4.5-4.5-4.5-7.5a4.5 4.5 0 0 1 9 0C15.5 12.5 11 17 11 17z" fill="var(--pin)"/><circle cx="11" cy="9.5" r="1.6" fill="#262626"/></svg>
      14 Orrin Lane Brighton 3187
    </li>
  </ul>
</section>

<section class="card card--back" aria-label="Business card back">
  <h2 class="stacked-name">
    <b>H</b>arwick<br><b>C</b>rossway<br><b>S</b>tudy<br><b>C</b>entre
  </h2>
  <ul class="program-list">
    <li>ELICOS with Boarding for U18 Students</li>
    <li>HSP-High School Preparation Program</li>
    <li>PSP- Primary School Preparation Program</li>
    <li>Junior Holiday Program &amp; Study Tours</li>
    <li>After School Tutoring</li>
    <li>Student Wellbeing and Counselling</li>
  </ul>
</section>

</body>
</html>
```